Now Leasing Banner

Looking for a banner that says the following information approx 4' x 30'

Now Leasing Maplewood Terrace 925-318-6054

Target Market(s)

Drive by traffic

Industry/Entity Type

Residential property management

Requirements
Must have
• Clear and readable from a distance

```html
<!DOCTYPE html>
<html lang="en">
<head>
<meta charset="utf-8">
<title>Now Leasing – Maplewood Terrace</title>
<link rel="stylesheet" href="https://fonts.googleapis.com/css2?family=Saira+Semi+Condensed:wght@700;800&display=swap">
<style>
  :root {
    --banner-blue: #3b55a5;
    --headline-red: #b01f26;
    --phone-yellow: #f8d714;
    --white: #ffffff;
    --ink: #0d0d0d;
  }
  html, body {
    margin: 0;
    padding: 0;
    width: 1200px;
    height: 160px;
    overflow: hidden;
    background: var(--banner-blue);
  }
  .banner {
    position: relative;
    width: 1200px;
    height: 160px;
    background: var(--banner-blue);
    overflow: hidden;
    font-family: "Saira Semi Condensed", "Arial Narrow", sans-serif;
  }
  .status-box {
    position: absolute;
    left: 33px;
    top: 11px;
    width: 528px;
    height: 72px;
    box-sizing: border-box;
    background: var(--headline-red);
    border: 4px solid var(--white);
  }
  .phone-pill {
    position: absolute;
    left: 636px;
    top: 21px;
    width: 620px;
    height: 110px;
    box-sizing: border-box;
    background: var(--phone-yellow);
    border: 5px solid var(--white);
    border-radius: 55px;
  }
  .banner-text {
    position: absolute;
    left: 0;
    top: 0;
    width: 1200px;
    height: 160px;
  }
  .banner-text text {
    font-family: "Saira Semi Condensed", "Arial Narrow", sans-serif;
    font-weight: 800;
  }
  .status-label { fill: var(--white); font-size: 58px; }
  .property-name { fill: var(--white); font-size: 80px; }
  .phone-number { fill: var(--ink); font-size: 74px; }
</style>
</head>
<body>
  <div class="banner">
    <div class="status-box"></div>
    <div class="phone-pill"></div>
    <svg class="banner-text" viewBox="0 0 1200 160" width="1200" height="160">
      <text class="status-label" x="113" y="70" textLength="368" lengthAdjust="spacingAndGlyphs">NOW LEASING</text>
      <text class="property-name" x="35" y="150" textLength="526" lengthAdjust="spacingAndGlyphs">MAPLEWOOD TERRACE</text>
      <text class="phone-number" x="694" y="99" textLength="467" lengthAdjust="spacingAndGlyphs">925-318-6054</text>
    </svg>
  </div>
</body>
</html>
```